Animal Feed Bag Packaging Design

The task is to design a livestock feed bag. These are 18"x32" and typically hold 50 LBS of feed. This design will be on all of the packaging for our feed bags. These feed bags will be sold in local feed and hardware stores and will hold a variety of different feed products for all classes of livestock. The bags will be double sided. I would like the back side to remain consistent, but I would like the front of the bag to have 4 different varieties that share the same layout, but incorporate different titles and possible graphics. The Categories will be:
- "Poultry Feed" This will be for all classes of poultry
- "Hog Feed" This will be for all classes of hogs
- "Mixed Feed" This will be a sort of catch all design that will be used for a variety of different types of livestock feed (cows, goats, sheep, rabbits)
- "Feed & Grain": This will also be a miscelaneous category that will be used for whole grains and feeds that can be used across multiple animal types.

I have attached many photos that may or may not be used, but that may help to portray our operation and what we do.

Target Market(s)

Backyard Hobby Farmers and Livestock Enthusists

Industry/Entity Type

Agriculture

Font styles to use
Serif

Colors

Designer to choose colors to be used in the design.

Requirements
Must have
• Must contain our logo and have a strong brand presence for "Calloway Kin's Feed". Each bag needs to contain the the following on either the front or backside of the bag. Calloway Kin's Feed - 214 North Willow Lane Brackmoor Utah, 61392 - 608 271 5519 - callowaykinsfeed.example
Nice to have
• Our brand is built around these factors that could be incorporated into the design: Locally Milled, Quality Ingredients, Balanced Nutrition, Family Owned & Operated Est. 2017. Home delivery is also a core competency of our operation. I will attach a few images of our farm where we operate at that may be incorporated if it fits the style.

```html
<!DOCTYPE html>
<html lang="en">
<head>
<meta charset="utf-8">
<title>Calloway Kin's Feed – Poultry Feed Bag Front</title>
<link rel="stylesheet" href="https://fonts.googleapis.com/css2?family=Archivo+Black&family=Montserrat:wght@500;600&display=swap">
<style>
  :root {
    --cream: #fcf4e0;
    --cream-text: #fbf3df;
    --olive: #6b7556;
    --gold: #c69c2e;
    --tick: #e3b33a;
    --copy: #9a8a45;
    --sky: #7fb4e6;
    --field: #6f9a3e;
  }
  * { margin: 0; padding: 0; box-sizing: border-box; }
  html, body { width: 1200px; height: 2260px; overflow: hidden; background: var(--cream); }
  .bag-front { position: relative; width: 1200px; height: 2260px; background: var(--cream); }
  .bag-shapes { position: absolute; inset: 0; }

  .brand-badge {
    position: absolute; left: 380px; top: 143px; width: 440px; height: 440px;
    display: flex; align-items: center; justify-content: center; text-align: center;
    font-family: "Archivo Black", sans-serif; font-size: 44px; line-height: 1.15;
    color: var(--cream-text); letter-spacing: 1px;
  }

  .title-block {
    position: absolute; left: 101px; top: 1420px; width: 996px;
    text-align: center; color: var(--cream-text); font-family: "Archivo Black", sans-serif;
  }
  .established {
    display: flex; align-items: center; justify-content: center; gap: 22px;
    font-size: 44px; letter-spacing: 12px; line-height: 1;
  }
  .established::before, .established::after {
    content: ""; width: 270px; height: 4px; background: var(--cream-text);
  }
  .product-name { font-size: 156px; line-height: 0.98; letter-spacing: -2px; margin-top: 22px; }

  .selling-points {
    position: absolute; top: 1955px; list-style: none;
    font-family: "Montserrat", sans-serif; font-weight: 600; font-size: 33px;
    line-height: 1.05; color: var(--copy); text-transform: uppercase;
  }
  .selling-points li { position: relative; padding-left: 52px; margin-bottom: 36px; }
  .selling-points li svg { position: absolute; left: 0; top: 4px; width: 24px; height: 24px; }
  .points-left { left: 128px; }
  .points-right { left: 770px; }

  .net-weight {
    position: absolute; left: 430px; top: 1925px; width: 310px; text-align: center;
    font-family: "Archivo Black", sans-serif; color: var(--gold);
  }
  .weight-number { font-size: 236px; line-height: 0.9; letter-spacing: -6px; }
  .weight-unit { font-size: 62px; line-height: 1; margin-left: 90px; }
</style>
</head>
<body>
<main class="bag-front">
  <svg class="bag-shapes" viewBox="0 0 1200 2260" width="1200" height="2260" aria-hidden="false">
    <defs>
      <linearGradient id="farm-scene" x1="0" y1="0" x2="0" y2="1">
        <stop offset="0" stop-color="#5a9be0"/>
        <stop offset="0.45" stop-color="#bcd9f0"/>
        <stop offset="0.62" stop-color="#6f9a3e"/>
        <stop offset="0.85" stop-color="#8a7a4a"/>
        <stop offset="1" stop-color="#7a6a44"/>
      </linearGradient>
    </defs>
    <!-- top bands -->
    <path class="band-gold" d="M0,285 Q600,190 1200,285 V325 Q600,230 0,325 Z" fill="var(--gold)"/>
    <path class="band-olive" d="M0,325 Q600,230 1200,325 V412 Q600,317 0,412 Z" fill="var(--olive)"/>
    <!-- farm photo area -->
    <path class="farm-photo" role="img" aria-label="Photo of a brown hen walking through green grass on a sunny farm with blue sky"
          d="M0,410 Q600,315 1200,410 V1512 Q600,1600 0,1512 Z" fill="url(#farm-scene)"/>
    <!-- lower bands -->
    <path class="band-olive" d="M0,1510 Q600,1598 1200,1510 V1590 Q600,1678 0,1590 Z" fill="var(--olive)"/>
    <path class="band-gold" d="M0,1590 Q600,1678 1200,1590 V1655 Q600,1743 0,1655 Z" fill="var(--gold)"/>
    <!-- brand circle -->
    <circle cx="600" cy="363" r="222" fill="var(--olive)"/>
    <circle cx="600" cy="363" r="180" fill="none" stroke="var(--cream-text)" stroke-width="4"/>
    <!-- title panel -->
    <path class="title-panel" d="M101,1395 H1097 V1805 Q600,1905 101,1805 Z" fill="var(--olive)"/>
  </svg>

  <div class="brand-badge">Calloway<br>Kin's Feed</div>

  <header class="title-block">
    <p class="established">EST. 2017</p>
    <h1 class="product-name">POULTRY<br>FEED</h1>
  </header>

  <ul class="selling-points points-left">
    <li><svg viewBox="0 0 24 24"><circle cx="12" cy="12" r="12" fill="var(--tick)"/><path d="M6.5 12.5l3.5 3.5 7.5-8" stroke="#fff" stroke-width="2.6" fill="none"/></svg>Locally<br>Milled</li>
    <li><svg viewBox="0 0 24 24"><circle cx="12" cy="12" r="12" fill="var(--tick)"/><path d="M6.5 12.5l3.5 3.5 7.5-8" stroke="#fff" stroke-width="2.6" fill="none"/></svg>Quality<br>Ingredients</li>
  </ul>

  <div class="net-weight">
    <div class="weight-number">50</div>
    <div class="weight-unit">LBS</div>
  </div>

  <ul class="selling-points points-right">
    <li><svg viewBox="0 0 24 24"><circle cx="12" cy="12" r="12" fill="var(--tick)"/><path d="M6.5 12.5l3.5 3.5 7.5-8" stroke="#fff" stroke-width="2.6" fill="none"/></svg>Balanced<br>Nutrition</li>
    <li><svg viewBox="0 0 24 24"><circle cx="12" cy="12" r="12" fill="var(--tick)"/><path d="M6.5 12.5l3.5 3.5 7.5-8" stroke="#fff" stroke-width="2.6" fill="none"/></svg>Family Owned<br>&amp; Operated</li>
  </ul>
</main>
</body>
</html>
```